Verdant Rooms Stationary Set

Verdant Rooms is a bespoke interior design firm set to provide services to VIP clients with elegance and minimalism is the main theme for our stationary set. We require a full stationary set covering A4 letterhead, A4 & A3 envelopes, business cards, USB's, CDs, email signature and any other item the designer sees fit. logo is already designed and finalized, and we require the designer to use it as is without modifying the logo.

Address to be used on letterhead / business cards ...etc shall be as follows:

Phone : +971 2 518 3076
P.O. Box : 318947
Address: Block C&D, Bldg. 27, Court 14, Abu Dhabi, United Arab Emirates
Website: www.verdantrooms.example

Target Market(s)

VIP Clients

Industry/Entity Type

Interior Design

Font styles to use
Other font styles liked:
• something to be unique

Colors

Designer to choose colors to be used in the design.

Requirements
Must have
• Elegant, minimalistic
Nice to have
• Simple yet elegant design having a sharp yet clean cut format
Should not have
• No additional colours, just colours that are used in the logo (silver, black or gold)

```html
<!DOCTYPE html>
<html lang="en">
<head>
<meta charset="utf-8">
<title>Verdant Rooms – Email Signature</title>
<link rel="stylesheet" href="https://fonts.googleapis.com/css2?family=Arimo:wght@400;700&display=swap">
<style>
  :root {
    --page: #ffffff;
    --ink: #1a1a1a;
    --gold: #b8965a;
  }
  * { margin: 0; padding: 0; box-sizing: border-box; }
  html, body {
    width: 1200px;
    height: 1048px;
    overflow: hidden;
    background: var(--page);
    font-family: "Arimo", Arial, sans-serif;
    color: var(--ink);
  }
  .signature {
    position: absolute;
    left: 50px;
    top: 395px;
    width: 1100px;
    height: 258px;
  }
  .sender-name {
    position: absolute;
    left: 0;
    top: 0;
    font-size: 29px;
    font-weight: 700;
    letter-spacing: 0.2px;
    color: var(--gold);
    text-transform: uppercase;
  }
  .sender-role {
    position: absolute;
    left: 0;
    top: 36px;
    font-size: 24px;
    font-weight: 400;
  }
  .brand-name {
    position: absolute;
    left: 0;
    top: 200px;
    width: 290px;
    font-size: 34px;
    font-weight: 400;
    color: var(--ink);
    white-space: nowrap;
  }
  .divider {
    position: absolute;
    left: 314px;
    top: 206px;
    width: 10px;
    height: 54px;
    background: var(--gold);
  }
  .contact {
    position: absolute;
    left: 350px;
    top: 202px;
    font-style: normal;
    font-size: 22px;
    line-height: 30px;
  }
  .contact-line {
    display: block;
    white-space: nowrap;
  }
</style>
</head>
<body>
  <section class="signature">
    <p class="sender-name">Nadim Rayes</p>
    <p class="sender-role">General Manager</p>
    <p class="brand-name">Verdant Rooms</p>
    <div class="divider"></div>
    <address class="contact">
      <span class="contact-line">Block C&amp;D, Bldg. 27, Court 14, Abu Dhabi, United Arab Emirates</span>
      <span class="contact-line">P.O. Box: 318947 · Tel: +971 2 518 3076 · www.verdantrooms.example</span>
    </address>
  </section>
</body>
</html>
```